Wine Label for a wine from Tuscany, Italy

We need a wine label for a white and red wine, can be the same label or can be somewhat differentiated with any variation you feel would be good.. These two wines come from Tuscany, Italy. Wine labels from Tuscany Italy tend to be traditional. We are open to traditional looking labels but also more modern, eye catching too. We want to convey a sense of elegance, importance, great wine. I am attaching some examples of labels we like from Tuscany, also a label that was designed for us recently by one of you, which we LOVE. No wine glasses, wine bottles or grapes featured on the label please. We tend to like the white background. No blue please.

Target Market(s)

More women than men purchase wine, but it needs to appeal to both sexes.

Requirements
Must have
• Wine Name: Corte L' or Corte l'
• Type/Varletal: Rosso Toscano (White is Vermentino)
• Vintage (year): 2018
• That is all the text we want on the label, thanks
Nice to have
• Clean, something that makes someone want to grab this wine bottle off the shelf!
Should not have
• Images of Wine glass, wine bottles, grapes
• Do not use the color blue please.

```html
<!DOCTYPE html>
<html lang="it">
<head>
<meta charset="utf-8">
<title>Corte L' — Rosso Toscano 2018</title>
<link rel="stylesheet" href="https://fonts.googleapis.com/css2?family=Cinzel:wght@400;500&display=swap">
<style>
  :root {
    --backdrop: #f4f4f7;
    --label-white: #ffffff;
    --label-charcoal: #3d3b3c;
    --label-charcoal-deep: #333132;
    --gold: #c9a660;
    --ink-light: #f5f3ef;
  }
  * { margin: 0; padding: 0; box-sizing: border-box; }
  html, body {
    width: 1107px;
    height: 1200px;
    overflow: hidden;
    background: var(--backdrop);
  }
  .canvas {
    position: relative;
    width: 1107px;
    height: 1200px;
    display: flex;
    align-items: center;
    justify-content: center;
  }
  .wine-label {
    position: relative;
    width: 760px;
    height: 640px;
    background: linear-gradient(160deg, var(--label-charcoal) 0%, var(--label-charcoal-deep) 100%);
    box-shadow: 0 18px 40px rgba(0, 0, 0, 0.12);
    overflow: hidden;
  }
  .label-band {
    position: absolute;
    top: 0;
    left: 0;
    width: 100%;
    height: 190px;
    background: var(--label-white);
  }
  .label-rule {
    position: absolute;
    top: 190px;
    left: 0;
    width: 100%;
    height: 4px;
    background: var(--gold);
  }
  .label-text {
    position: absolute;
    top: 250px;
    left: 0;
    width: 100%;
    text-align: center;
    font-family: "Cinzel", serif;
  }
  .wine-name {
    font-size: 84px;
    font-weight: 500;
    color: var(--gold);
    letter-spacing: 0.04em;
    line-height: 1;
  }
  .wine-type {
    margin-top: 44px;
    font-size: 30px;
    font-weight: 400;
    color: var(--ink-light);
    letter-spacing: 0.22em;
  }
  .wine-vintage {
    margin-top: 26px;
    font-size: 30px;
    font-weight: 400;
    color: var(--ink-light);
    letter-spacing: 0.9em;
    padding-left: 0.9em;
  }
</style>
</head>
<body>
  <main class="canvas">
    <section class="wine-label">
      <div class="label-band"></div>
      <div class="label-rule"></div>
      <div class="label-text">
        <h1 class="wine-name">Corte L'</h1>
        <p class="wine-type">Rosso Toscano</p>
        <p class="wine-vintage">2018</p>
      </div>
    </section>
  </main>
</body>
</html>
```